Meadowtail Pet Business Card

We need a business card designed with two sides to it. I would like the front of the card to be mostly graphic and the back of the card to have the bullet points of our pet food.

I don't have a telephone number for the business yet so just leave a space for a toll free number. (800) xxx-xxxx.

Thanks,

Tobias

Combination Diet
Chicken Diet
Beef Diet
Lamb Diet

Website:  www.meadowtailpet-example.net

email:  rwelby@meadowtailpet-example.net

Direct - 347-xxx-xxxx
Toll Free - xxx-xxx-xxxx

www.meadowtailpet-example.net

Ravi Welby (Example)
Customer Experience Officer

rwelby@meadowtailpet-example.net
Direct - (347) xxx-xxxx

Sales Inquiries - (800) xxx-xxxx

All,

Please include the following items on the back of the business card.

Combination Diet
Chicken Diet
Beef Diet
Lamb Diet
 

Thanks,

Tobias

All, I will also want a QR code on the front or back of the card that can be scanned by a smart phone with our individual contact information.  Thanks, Tobias

Industry/Entity Type

Pet

```html
<!DOCTYPE html>
<html lang="en">
<head>
<meta charset="utf-8">
<title>Meadowtail Pet Business Card</title>
<link rel="stylesheet" href="https://fonts.googleapis.com/css2?family=Exo+2:wght@300;400;600;700;800&display=swap">
<style>
  :root {
    --stage: #d6d6d6;
    --card-white: #ffffff;
    --card-dark: #1f1f1f;
    --ink: #1a1a1a;
    --ink-soft: #3a3a3a;
    --accent-red: #d3332b;
    --faint-grey: #ededed;
    --tree-grey: #c9c9c9;
    --faint-dark: #262626;
    --silhouette: #141414;
    --sun-pale: #fdf7e6;
    --band: #111111;
    --white: #ffffff;
  }
  * { margin: 0; padding: 0; box-sizing: border-box; }
  html, body { width: 1200px; height: 717px; overflow: hidden; }
  body {
    background: var(--stage);
    font-family: "Exo 2", sans-serif;
    position: relative;
  }
  .card {
    position: absolute;
    left: 316px;
    width: 535px;
    height: 320px;
    overflow: hidden;
  }
  .card-front { top: 31px; background: var(--card-white); }
  .card-back { top: 374px; background: var(--card-dark); }

  /* front decoration */
  .sun-decor {
    position: absolute; left: 140px; top: 68px;
    width: 195px; height: 195px; border-radius: 50%;
    background: radial-gradient(circle at 50% 50%, var(--sun-pale) 0%, var(--sun-pale) 60%, rgba(253,247,230,0) 72%);
  }
  .tree-decor {
    position: absolute; left: 345px; top: 112px;
    width: 190px; height: 200px;
    border-radius: 90px 40px 0 0;
    background:
      linear-gradient(180deg, rgba(201,201,201,.75) 0%, rgba(201,201,201,.45) 30%, rgba(220,220,220,.25) 60%, rgba(255,255,255,0) 100%);
  }
  .dog-faint {
    position: absolute; left: 0; top: 222px;
    width: 90px; height: 88px;
    border-radius: 40px 50px 0 0;
    background: linear-gradient(180deg, rgba(225,225,225,.9), rgba(236,236,236,.6));
  }
  .wordmark-decor {
    position: absolute; left: 260px; top: 238px;
    font-size: 80px; font-weight: 800; letter-spacing: -2px;
    color: var(--faint-grey); white-space: nowrap; line-height: 1;
  }

  .brand {
    position: absolute; left: 30px; top: 28px; width: 225px;
    text-align: center;
  }
  .brand-name {
    display: flex; align-items: center; justify-content: center; gap: 8px;
    font-size: 27px; font-weight: 800; color: var(--ink); line-height: 1;
    margin-top: 52px;
  }
  .brand-mark { width: 16px; height: 16px; background: var(--accent-red); }
  .brand-tagline {
    margin-top: 24px; font-size: 9.5px; font-weight: 600;
    letter-spacing: 1.6px; color: var(--ink-soft); text-transform: uppercase;
  }
  .person {
    position: absolute; right: 38px; top: 30px; text-align: right;
  }
  .person-name { font-size: 23px; line-height: 1; color: var(--ink); }
  .person-name .first { font-weight: 300; color: var(--accent-red); }
  .person-name .last { font-weight: 700; }
  .person-title { font-size: 12.5px; margin-top: 2px; color: var(--ink-soft); }
  .contacts {
    position: absolute; left: 34px; top: 183px; list-style: none;
  }
  .contacts li {
    display: flex; align-items: center; gap: 6px;
    height: 22px; font-size: 13px; color: var(--ink);
  }
  .contacts svg { width: 16px; height: 14px; fill: var(--accent-red); }
  .sales-line {
    position: absolute; left: 34px; top: 263px;
    font-size: 13px; color: var(--ink);
  }
  .sales-line .label { color: var(--accent-red); }
  .front-band {
    position: absolute; left: 0; bottom: 0; width: 100%; height: 10px;
    background: var(--band);
  }

  /* back */
  .back-wordmark-top {
    position: absolute; left: 270px; top: -40px;
    font-size: 150px; font-weight: 800; color: var(--faint-dark);
    line-height: 1; white-space: nowrap;
  }
  .back-wordmark-bottom {
    position: absolute; left: 200px; top: 175px;
    font-size: 150px; font-weight: 800; color: var(--faint-dark);
    line-height: 1; white-space: nowrap; letter-spacing: -3px;
  }
  .dog-decor {
    position: absolute; left: 292px; top: 42px;
    width: 243px; height: 234px;
    border-radius: 60px 80px 4px 4px;
    background: linear-gradient(180deg, var(--silhouette) 0%, #151515 70%, #181818 100%);
  }
  .diet-list {
    position: absolute; left: 46px; top: 64px; list-style: none;
  }
  .diet-list li {
    display: flex; align-items: center; gap: 11px;
    height: 47.5px; font-size: 19px; font-weight: 700; color: var(--white);
  }
  .diet-list li::before {
    content: ""; width: 10px; height: 10px; border-radius: 50%;
    background: var(--accent-red);
  }
</style>
</head>
<body>
  <section class="card card-front">
    <div class="sun-decor" role="img" aria-label="Pale setting sun behind the brand"></div>
    <div class="tree-decor" role="img" aria-label="Faint grey acacia trees on the savanna"></div>
    <div class="dog-faint" role="img" aria-label="Faint silhouette of a sitting dog"></div>
    <div class="wordmark-decor" aria-hidden="true">meadowtail</div>

    <div class="brand">
      <div class="brand-name"><span class="brand-mark"></span>Meadowtail Pet</div>
      <div class="brand-tagline">100% Natural Raw Dog Food</div>
    </div>

    <div class="person">
      <div class="person-name"><span class="first">Ravi</span> <span class="last">Welby</span></div>
      <div class="person-title">Customer Experience Officer</div>
    </div>

    <ul class="contacts">
      <li>
        <svg viewBox="0 0 16 16"><path d="M8 1a7 7 0 1 0 0 14A7 7 0 0 0 8 1zm5.9 6.3h-2.6a11 11 0 0 0-.9-4.4 6 6 0 0 1 3.5 4.4zM8 2.3c.8 1 1.5 2.8 1.6 5H6.4c.1-2.2.8-4 1.6-5zM5.6 2.9a11 11 0 0 0-.9 4.4H2.1a6 6 0 0 1 3.5-4.4zM2.1 8.7h2.6a11 11 0 0 0 .9 4.4 6 6 0 0 1-3.5-4.4zM8 13.7c-.8-1-1.5-2.8-1.6-5h3.2c-.1 2.2-.8 4-1.6 5zm2.4-.6a11 11 0 0 0 .9-4.4h2.6a6 6 0 0 1-3.5 4.4z"/></svg>
        meadowtailpet-example.net
      </li>
      <li>
        <svg viewBox="0 0 16 12"><path d="M0 0h16v1.5L8 7 0 1.5z"/><path d="M0 3.2l8 5.5 8-5.5V12H0z"/></svg>
        rwelby@meadowtailpet-example.net
      </li>
      <li>
        <svg viewBox="0 0 16 14"><path d="M1 4c0-2 3-3 7-3s7 1 7 3v1.5h-3.5V4h-7v1.5H1z"/><path d="M3 7l2-2h6l2 2v6H3zm5 1.3a2 2 0 1 0 0 4 2 2 0 0 0 0-4z"/></svg>
        347-xxx-xxxx
      </li>
    </ul>

    <div class="sales-line"><span class="label">Sales Inquiries</span> - (800) xxx-xxxx</div>
    <div class="front-band"></div>
  </section>

  <section class="card card-back">
    <div class="back-wordmark-top" aria-hidden="true">pet</div>
    <div class="back-wordmark-bottom" aria-hidden="true">meadowtail</div>
    <div class="dog-decor" role="img" aria-label="Dark silhouette of a standing dog"></div>
    <ul class="diet-list">
      <li>Combination Diet</li>
      <li>Chicken Diet</li>
      <li>Beef Diet</li>
      <li>Lamb Diet</li>
    </ul>
  </section>
</body>
</html>
```